Cabling Business Graphic Design for Website

Hi,

We need a three pages designed for a cabling website: http://www.wirovant.com.au/

1.) Homepage
2.) Category Page
3.) Product Page

Wirovant is an online wholesaler of Server Racks and Cables.

Wirovant began in 2006 as an offshoot of a cabling installation company called Pyrosmel which has been around since 1993. Through Pyrosmel and the industry insight that gave use we saw the need for a direct, online wholesaler.

The problem we found the with the industry is the middle man. It seemed that industry suppliers were so obsessed with carving out distribution channels and establishing exclusive resellers and wholesalers that they began to alienate their products and price themselves out of the market.

Then came Wirovant - the first direct online data comms wholesaler to hit the industry.

We manufacture, import and sell direct - we have no middle men, keep our prices fair and our product range fresh.

Top three competitors:
Orbison Quarry - www.dulmep.com.au
Shelvantix - www.shelvantix.com.au
Brimtoll Messaging - www.brimtoll.net.au

Our range - we offer a massive range of products - we are always adding new and unique products.

Our Service - we have technical sales staff who are able to help with technical questions and provide advice on how to do things / what to buy - its not just a call centre situation.

We are able to custom manufacture cables and cabinets to suit specifications.

Its very easy to order from us, our turnaround time is 99% of the time 24 hours.

Please refer to the design brief file and the business uncovery for more information. The design brief files are quite specific so please ensure the design adheres to this brief.

Target Market(s)

IT Managers, Electricians, Network Integrators and IT companies.

They have a contract with schools and government departments to order their supplies. This is a massive section of their market.

Industry/Entity Type

Industry

Requirements
Must have
• Reinforce
* that the products adhere to government and industry certifications
* warranty / quality guarantee
* delivery details / stock availability
Nice to have
• Included in the Business Uncovery file
Should not have
• Included in the Business Uncovery

```html
<!DOCTYPE html>
<html lang="en">
<head>
<meta charset="utf-8">
<title>Wirovant – Server Racks &amp; Cables</title>
<link href="https://fonts.googleapis.com/css2?family=Arimo:wght@400;700&display=swap" rel="stylesheet">
<style>
:root{
  --red:#d9232a;
  --red-dark:#b5161c;
  --ink:#222;
  --muted:#444;
  --line:#d6d6d6;
  --panel:#ffffff;
  --head-top:#6e6466;
  --head-bot:#4a4244;
  --teal:#2b8fb0;
  --footer:#1c1c1c;
  --footer-2:#111;
  --tile-dark:#1e1e1e;
}
*{box-sizing:border-box;margin:0;padding:0}
html,body{width:1200px;height:1198px;overflow:hidden}
body{font-family:"Arimo",Arial,sans-serif;color:var(--ink);background:#fff;position:relative}

/* header */
.site-header{position:absolute;left:0;top:0;width:1200px;height:161px;
  background:radial-gradient(ellipse at 55% 40%,#8a8082 0%,var(--head-top) 45%,var(--head-bot) 100%)}
.brand{position:absolute;left:141px;top:46px;display:flex;align-items:center;gap:10px}
.brand-dot{width:18px;height:18px;background:var(--red);border-radius:50%}
.brand-name{font-size:50px;font-weight:700;color:#fff;letter-spacing:-1px}
.search{position:absolute;left:439px;top:45px;width:311px;height:70px;background:#f4f4f4;
  border:1px solid #ccc;border-radius:5px;padding:10px 16px}
.search h2{font-size:13px;font-weight:400;color:#222;margin-bottom:4px}
.search-row{display:flex;height:23px;border:1px solid #ccc;border-radius:12px;background:#fff;overflow:hidden}
.search-row span{flex:1;font-size:11px;color:#999;padding:5px 9px}
.search-row b{width:83px;background:linear-gradient(#3aa6c8,var(--teal));color:#fff;font-weight:400;font-size:13px;
  text-align:center;line-height:23px;border-radius:12px}
.agent{position:absolute;left:784px;top:24px;width:93px;height:116px;border-radius:6px;border:2px solid #ddd;
  background:linear-gradient(#e8e8ea,#c9c9cd)}
.support{position:absolute;right:158px;top:36px;text-align:right;color:#fff;font-size:13px;line-height:17px}
.support .phone{font-size:23px;line-height:30px;margin:3px 0 4px}

/* nav */
.main-nav{position:absolute;left:142px;top:167px;width:900px;height:37px;border:1px solid #d4d4d4;border-radius:7px;
  background:linear-gradient(#fff,#ececec);display:flex;align-items:center;padding-left:5px;font-size:13.5px}
.main-nav a{color:#222;text-decoration:none;padding:0 11px}
.main-nav .sep{color:#555}
.main-nav .active{background:linear-gradient(#f04a4f,var(--red-dark));color:#fff;font-weight:700;border-radius:12px;
  padding:4px 16px;margin-right:6px}

/* panels */
.panel{position:absolute;background:var(--panel);border:1px solid #ddd;border-radius:6px;
  box-shadow:inset 0 -14px 14px -10px #e2e2e2}
.panel-title{font-size:17.5px;font-weight:400;color:#111}

.cat-list{list-style:none;margin:12px 16px 0 12px}
.cat-list li{font-size:11px;line-height:12.5px;padding:5px 0 5px 13px;border-bottom:1px solid var(--line);
  position:relative;white-space:nowrap;letter-spacing:.1px}
.cat-list li::before{content:"›";position:absolute;left:0;top:4px;font-size:12px}
.cat-list li:last-child{border-bottom:0}

.cards{display:flex;gap:6px;justify-content:center;margin-top:12px}
.card-mark{width:44px;height:27px;border:1px solid #999;display:flex;align-items:center;justify-content:center;
  font-size:10px;font-weight:700;color:#fff;background:#333}
.testimonial p{font-size:11.3px;line-height:16.9px;margin:20px 0 0 12px;width:150px}

.welcome p{font-size:11.3px;line-height:16.9px;color:#222;margin:14px 10px 0 9px}
.welcome .more{font-style:italic;margin-top:14px;display:block}

.tile{position:absolute;width:131px;border:1px solid #ccc;background:#fff}
.tile .img{height:105px;margin:2px}
.tile-label{position:absolute;width:131px;height:29px;background:linear-gradient(#3a3a3a,var(--tile-dark));color:#fff;
  font-size:11px;text-align:center;line-height:25px;border:2px solid #ddd}

.section-title{position:absolute;left:328px;top:605px;font-size:17.5px;font-weight:400;color:#111}
.prod{position:absolute;width:131px}
.prod .pic{height:108px;border:1px solid #ccc;position:relative}
.prod .pic span{position:absolute;left:0;right:0;bottom:0;height:22px;background:rgba(225,225,225,.85);
  text-align:center;font-size:13.5px;line-height:22px;color:#222;letter-spacing:-.3px;white-space:nowrap}
.buy{display:flex;margin-top:7px;height:24px;border:1px solid #ccc;border-radius:5px;overflow:hidden;font-size:11px}
.buy .price{background:var(--red);color:#fff;width:42px;text-align:center;line-height:22px}
.buy .add{flex:1;background:linear-gradient(#fff,#e6e6e6);display:flex;align-items:center;justify-content:center;gap:5px;letter-spacing:-.3px}
.info{display:block;margin:7px auto 0;width:50px;height:14px;border:1px solid #bbb;border-radius:7px;
  background:linear-gradient(#fff,#e2e2e2);font-size:10px;text-align:center;line-height:12px;letter-spacing:-.3px}

.cart-box{position:absolute;left:881px;top:225px;width:156px;height:96px;border:1px solid #ccc;border-radius:5px;background:#fff;overflow:hidden}
.cart-title{display:flex;align-items:center;gap:6px;padding:8px 0 0 10px;height:34px;color:var(--red);
  font-size:18px;font-style:italic;font-family:Georgia,serif;white-space:nowrap}
.cart-grid{display:grid;grid-template-columns:1fr 1fr;gap:2px;margin:8px 3px 0}
.cart-grid span{background:#ededed;font-size:11px;text-align:center;padding:4px 0;line-height:13px;white-space:nowrap}
.why{position:absolute;left:881px;top:333px;width:156px;height:70px;border:1px solid #ccc;border-radius:5px;
  padding:5px 0 0 4px;font-size:16px;line-height:18px;color:#111;white-space:nowrap;overflow:hidden}
.why b{color:var(--red);font-size:20px}

.cert-shape{position:absolute;background:#d9d9d9}
.cert-text{position:absolute;font-size:11.5px;line-height:17px;color:#111}

.mail p{font-size:11.5px;line-height:17px;margin:16px 0 0 13px;width:150px}
.field{margin:10px 0 0 10px;width:150px;height:24px;border:1px solid #ccc;font-size:10.5px;color:#444;padding:6px 6px}

/* footer */
.site-footer{position:absolute;left:0;top:995px;width:1200px;height:165px;background:linear-gradient(#262626,var(--footer))}
.fcol{position:absolute;top:10px;color:#fff}
.fcol h3{font-size:13px;font-weight:400;line-height:17px;letter-spacing:.3px}
.fcol ul{list-style:none;margin-top:4px}
.fcol li{font-size:11.3px;line-height:17px;padding-left:13px;position:relative;letter-spacing:.2px}
.fcol li::before{content:"›";position:absolute;left:2px}
.fdiv{position:absolute;top:5px;height:150px;border-left:1px dotted #555}
.copyright{position:absolute;left:0;top:1160px;width:1200px;height:38px;background:var(--footer-2);
  color:#fff;font-size:11.5px;text-align:center;line-height:38px}
</style>
</head>
<body>

<header class="site-header">
  <div class="brand"><span class="brand-name">Wirovant</span><span class="brand-dot"></span></div>
  <div class="search">
    <h2>SEARCH</h2>
    <div class="search-row"><span>Search Term...</span><b>Search</b></div>
  </div>
  <div class="agent" role="img" aria-label="Portrait of a live chat support specialist"></div>
  <div class="support">
    <div>Need Support ? Speak to<br>Our Live Chat specialist</div>
    <div class="phone">001 555 0148</div>
    <div>Mon-Fri 09am-05pm AEST</div>
  </div>
</header>

<nav class="main-nav">
  <a class="active">Home</a>
  <a>About Us</a><span class="sep">|</span>
  <a>Shipping</a><span class="sep">|</span>
  <a>Payments</a><span class="sep">|</span>
  <a>OurCatalogue</a><span class="sep">|</span>
  <a>Wholesale Outlets</a><span class="sep">|</span>
  <a>Education / Government</a><span class="sep">|</span>
  <a>Account/Login</a>
</nav>

<!-- left column -->
<aside class="panel" style="left:142px;top:214px;width:169px;height:414px;padding-top:8px">
  <h2 class="panel-title" style="margin-left:14px">Products Ex GST</h2>
  <ul class="cat-list">
    <li>Cable</li><li>Data Products</li><li>Fibre Products</li><li>COAX Products</li>
    <li>Electrical Products</li><li>Telephone &amp; Voice</li><li>Tools &amp; Testers</li>
    <li>Computer Cables</li><li>Switches &amp; Hardware</li><li>AV Wall plates &amp; Inserts</li>
    <li>Plasma &amp; LCD Brackets</li><li>Cable Ducting Conduit</li><li>Server Racks/ Networks</li>
    <li>Cabinets</li><li>Cable Management</li><li>Cable Labels</li>
  </ul>
</aside>

<aside class="panel" style="left:142px;top:643px;width:169px;height:126px;padding-top:12px;text-align:center">
  <h2 class="panel-title" style="line-height:17px">Secure Credit Card<br>Process</h2>
  <div class="cards">
    <span class="card-mark">Cardora</span>
    <span class="card-mark">Vexa</span>
    <span class="card-mark">Paylex</span>
  </div>
</aside>

<aside class="panel testimonial" style="left:142px;top:788px;width:169px;height:172px;padding-top:9px">
  <h2 class="panel-title" style="text-align:center">Testimonial</h2>
  <p>Can I also pass on how happy I am with Wirovant's service - I ordered late yesterday and received the delivery this morning - very impressed!</p>
</aside>

<!-- centre column -->
<section class="panel welcome" style="left:321px;top:216px;width:542px;height:187px;padding-top:5px">
  <h1 class="panel-title" style="margin-left:7px">Welcome To Our Website</h1>
  <p>Lorem Ipsum is simply dummy text of the printing and typesetting industry. Lorem Ipsum has been the industry's standard dummy text ever since the 1500s, when an unknown printer took a galley of type and scrambled it to make a type specimen book. It has survived not only five centuries, but also the leap into electronic typesetting, remaining essentially unchanged. It was popularised in the 1960s with the release of Fontrell sheets containing Lorem Ipsum passages, and more recently with desktop publishing software like Pagewright Studio including versions of Lorem Ipsum.
  <span class="more">Read More</span></p>
</section>

<div class="tile" style="left:324px;top:437px"><div class="img" role="img" aria-label="Red network cable with exposed twisted pairs" style="background:linear-gradient(#fafafa,#f0e6e6)"></div></div>
<div class="tile" style="left:458px;top:437px"><div class="img" role="img" aria-label="Office cable management installation" style="background:linear-gradient(#b36a4a,#9aa0a0)"></div></div>
<div class="tile" style="left:593px;top:437px"><div class="img" role="img" aria-label="Patch panel with blue data leads" style="background:linear-gradient(#2a3a48,#3e8fa8)"></div></div>
<div class="tile" style="left:727px;top:437px"><div class="img" role="img" aria-label="Black server rack cabinet" style="background:linear-gradient(#2a2a2a,#111)"></div></div>
<div class="tile-label" style="left:324px;top:550px">Cables</div>
<div class="tile-label" style="left:458px;top:550px">Cable Management</div>
<div class="tile-label" style="left:593px;top:550px">Data Products</div>
<div class="tile-label" style="left:727px;top:550px">Server Rack Cabinets</div>

<h2 class="section-title">Top Selling Products</h2>

<svg width="0" height="0" style="position:absolute">
  <symbol id="cart" viewBox="0 0 16 14"><path d="M1 2h3l2 7h7l2-5H5" fill="none" stroke="#c22" stroke-width="1.6"/><circle cx="7" cy="12" r="1.3" fill="#c22"/><circle cx="12" cy="12" r="1.3" fill="#c22"/></symbol>
</svg>

<div class="prod" style="left:324px;top:634px">
  <div class="pic" role="img" aria-label="Coiled colourful network cables" style="background:linear-gradient(#fff,#f3b08c 50%,#7ec3d8)"><span>Network Cable</span></div>
  <div class="buy"><span class="price">$18.00</span><span class="add"><svg width="16" height="14"><use href="#cart"/></svg>Add to cart</span></div>
  <span class="info">More Info</span>
</div>
<div class="prod" style="left:458px;top:634px">
  <div class="pic" role="img" aria-label="White HDMI switch box" style="background:linear-gradient(#fafafa,#dcdcdc)"><span>HDMI Cable</span></div>
  <div class="buy"><span class="price">$18.00</span><span class="add"><svg width="16" height="14"><use href="#cart"/></svg>Add to cart</span></div>
  <span class="info">More Info</span>
</div>
<div class="prod" style="left:593px;top:634px">
  <div class="pic" role="img" aria-label="Fibre optic patch leads" style="background:linear-gradient(#fff,#e8ecf2)"><span>Cables</span></div>
  <div class="buy"><span class="price">$18.00</span><span class="add"><svg width="16" height="14"><use href="#cart"/></svg>Add to cart</span></div>
  <span class="info">More Info</span>
</div>
<div class="prod" style="left:727px;top:634px">
  <div class="pic" role="img" aria-label="Close-up of coloured cable connectors" style="background:linear-gradient(90deg,#c9302a,#3f8a3a,#2f6fa0)"><span>Cables</span></div>
  <div class="buy"><span class="price">$18.00</span><span class="add"><svg width="16" height="14"><use href="#cart"/></svg>Add to cart</span></div>
  <span class="info">More Info</span>
</div>

<div class="prod" style="left:324px;top:809px">
  <div class="pic" role="img" aria-label="Red network cable with exposed twisted pairs" style="background:linear-gradient(#fafafa,#f0e6e6)"><span>Cables</span></div>
  <div class="buy"><span class="price">$18.00</span><span class="add"><svg width="16" height="14"><use href="#cart"/></svg>Add to cart</span></div>
  <span class="info">More Info</span>
</div>
<div class="prod" style="left:458px;top:809px">
  <div class="pic" role="img" aria-label="Office cable management installation" style="background:linear-gradient(#b36a4a,#9aa0a0)"><span>Cable Management</span></div>
  <div class="buy"><span class="price">$18.00</span><span class="add"><svg width="16" height="14"><use href="#cart"/></svg>Add to cart</span></div>
  <span class="info">More Info</span>
</div>
<div class="prod" style="left:593px;top:809px">
  <div class="pic" role="img" aria-label="Patch panel with blue data leads" style="background:linear-gradient(#2a3a48,#3e8fa8)"><span>Data Products</span></div>
  <div class="buy"><span class="price">$18.00</span><span class="add"><svg width="16" height="14"><use href="#cart"/></svg>Add to cart</span></div>
  <span class="info">More Info</span>
</div>
<div class="prod" style="left:727px;top:809px">
  <div class="pic" role="img" aria-label="Black server rack cabinet" style="background:linear-gradient(#2a2a2a,#111)"><span>Server Rack Cabinets</span></div>
  <div class="buy"><span class="price">$18.00</span><span class="add"><svg width="16" height="14"><use href="#cart"/></svg>Add to cart</span></div>
  <span class="info">More Info</span>
</div>

<!-- right column -->
<aside class="panel" style="left:873px;top:214px;width:169px;height:198px"></aside>
<div class="cart-box">
  <div class="cart-title">
    <svg width="24" height="20" viewBox="0 0 16 14"><path d="M1 2h3l2 7h7l2-5H5" fill="none" stroke="#222" stroke-width="1.4"/><circle cx="7" cy="12" r="1.3" fill="#222"/><circle cx="12" cy="12" r="1.3" fill="#222"/></svg>
    Shopping Cart
  </div>
  <div class="cart-grid">
    <span>View Cart</span><span>CheckOut</span><span>Contents</span><span>Sub Totals</span>
  </div>
</div>
<div class="why">Why <b>Wirovant?</b><br>...reasons to deal<br>with Wirovant</div>

<aside class="panel" style="left:873px;top:424px;width:169px;height:303px;padding:8px 0 0 11px">
  <h2 style="font-size:14px;font-weight:400;line-height:17px">Certificate &amp;<br>Quality Assurance</h2>
  <div class="cert-shape" style="left:15px;top:50px;width:54px;height:70px"></div>
  <div class="cert-shape" style="left:8px;top:130px;width:66px;height:70px"></div>
  <div class="cert-text" style="left:84px;top:116px">AS/NZS ISO<br>9001-2008</div>
  <div class="cert-shape" style="left:8px;top:233px;width:56px;height:56px;border-radius:50%"></div>
  <div class="cert-text" style="left:79px;top:256px">Education /<br>Government</div>
</aside>

<aside class="panel mail" style="left:873px;top:742px;width:169px;height:218px;padding-top:7px">
  <h2 style="font-size:14px;font-weight:400;margin-left:11px">Join Our Mailing List</h2>
  <p>Discover exclusive offers, products previews and much more</p>
  <div class="field">Email Address</div>
  <div class="field">Get Special Offer</div>
  <p style="margin-top:18px;text-align:center;width:auto;font-size:11px">We Value Your Privacy</p>
</aside>

<!-- footer -->
<footer class="site-footer">
  <div class="fcol" style="left:141px">
    <h3>SERVER RACKS / NETWORK<br>COMPUTER CABINETS</h3>
    <ul>
      <li>Network Cabinet &amp; Rack Mount Accesories</li>
      <li>Wall Mount Network Cabinets</li>
      <li>Half Height Floor Server Racks</li>
      <li>Full Height Server Racks</li>
      <li>Wall Mount Frames</li>
      <li>Network Cabinet Shelves</li>
    </ul>
  </div>
  <span class="fdiv" style="left:396px"></span>
  <div class="fcol" style="left:417px">
    <h3>CABLE MANAGEMENT</h3>
    <ul style="margin-top:12px">
      <li>Cable Floor Covers</li><li>Cable Management Rails</li><li>Cable Ties</li>
      <li>Cable Tray</li><li>Cable Management Baskets</li>
    </ul>
  </div>
  <span class="fdiv" style="left:603px"></span>
  <div class="fcol" style="left:642px">
    <h3>ETHERNET CABLES</h3>
    <ul style="margin-top:12px"><li>Cat 5E Cable</li><li>Cat 6 Cable</li></ul>
    <h3 style="margin-top:3px">PATCH PANELS</h3>
    <ul style="margin-top:8px"><li>Cat5e Patch Panel</li><li>Cat 6 Patch Panels</li></ul>
  </div>
  <span class="fdiv" style="left:806px"></span>
  <div class="fcol" style="left:843px">
    <h3>FIBRE PRODUCTS</h3>
    <ul style="margin-top:12px">
      <li>Multimode Fibre Optic Patch Cables</li>
      <li>Single Mode Fibre Optic Patch Leads</li>
      <li>Fibre Optic Cable</li>
    </ul>
  </div>
</footer>
<div class="copyright">Copyright 2011 Wirovant.com</div>

</body>
</html>
```